CREATIVE, BEAUTIFUL, STANDOUT BUSINESS CARD WITH LOGO DESIRED

Hello. I am a screenwriter, going to Hollywood soon to seek representation by agents and managers, as well as to pitch my screenplays and TV scripts to producers.

I need a CREATIVE, BEAUTIFUL, STANDOUT ONE-SIDED business card and LOGO with the following features:

Marcus Pell
Screenwriter
--- This part ("Marcus Pell" on one line, and "Screenwriter" on the next) should be an enticing logo, for which I need a separate file, so that I can also use it for branding on my website, social media, etc.
Then, as part of the same text set, under my name and profession should be my contact information:
Phone: 555 - 214 - 7386
Email: marcuspell@[login to view URL]
Website: [login to view URL]

The second text set should contain the following:

LOGLINE: A brilliant, shrewd Hollywood visionary joins forces with a talented, prolific screenwriter to create wonderful stories and make lots of money together. Make this your story at www.marcuspellwrites.com.

With this message, I am uploading two attachments:

1. My photo
2. The text sets the card should contain.

You can use your design flair and creativity to work with layout, colors and design.

It should be dynamic and, when the recipient of the business card is sifting through the 60 or so cards they received that day, it should stand out and help them remember me, and make them want to reach out.

By entering this contest, you agree that, if you win, I will receive the source file for the business card, and the source file for the logo, so that I can make future changes, as well as the rights to them, so I can use the logo on my website, social media, advertising, etc.

Feel free to ask questions.

Thank you for your help, and good luck to you!

Marcus

```html
<!DOCTYPE html>
<html lang="en">
<head>
<meta charset="utf-8">
<title>Marcus Pell – Screenwriter Business Card</title>
<link href="https://fonts.googleapis.com/css2?family=Great+Vibes&family=Roboto+Slab:wght@300;400&display=swap" rel="stylesheet">
<style>
  :root {
    --backdrop: #3b3b3d;
    --card-dark: #140e10;
    --card-edge: #0c0809;
    --mauve: #8d7070;
    --mauve-deep: #6e5555;
    --body-text: #d2c9c8;
    --link: #a06f74;
    --photo-top: #6b3716;
    --photo-mid: #4a2410;
    --photo-low: #4e1414;
    --photo-base: #2e0b0b;
  }
  * { box-sizing: border-box; margin: 0; padding: 0; }
  html, body {
    width: 1200px;
    height: 931px;
    overflow: hidden;
    background: var(--backdrop);
  }
  .canvas {
    position: relative;
    width: 1200px;
    height: 931px;
  }
  .business-card {
    position: absolute;
    left: 80px;
    top: 168px;
    width: 1040px;
    height: 594px;
    display: flex;
    background: var(--card-dark);
    box-shadow: 0 18px 40px rgba(0,0,0,0.45);
    border-right: 6px solid var(--card-edge);
  }
  .portrait {
    width: 420px;
    height: 100%;
    flex: none;
    background: linear-gradient(165deg, var(--photo-top) 0%, var(--photo-mid) 48%, var(--photo-low) 78%, var(--photo-base) 100%);
  }
  .details {
    flex: 1;
    padding: 50px 60px 0 60px;
    display: flex;
    flex-direction: column;
  }
  .brand {
    align-self: center;
    text-align: center;
  }
  .brand-name {
    font-family: "Great Vibes", cursive;
    font-size: 62px;
    line-height: 1;
    color: var(--mauve);
    font-weight: 400;
  }
  .brand-title {
    font-family: "Roboto Slab", serif;
    font-size: 14px;
    letter-spacing: 2px;
    color: var(--mauve);
    text-transform: uppercase;
    margin-top: 4px;
  }
  .logline {
    font-family: "Roboto Slab", serif;
    font-weight: 300;
    font-size: 19px;
    line-height: 1.4;
    color: var(--body-text);
    text-align: center;
    margin-top: 36px;
  }
  .logline .site { color: var(--link); }
  .contact-list {
    list-style: none;
    margin-top: 58px;
    margin-left: 60px;
    display: flex;
    flex-direction: column;
    gap: 16px;
  }
  .contact-item {
    display: flex;
    align-items: center;
    gap: 16px;
    font-family: "Roboto Slab", serif;
    font-weight: 300;
    font-size: 20px;
    color: var(--body-text);
  }
  .contact-icon {
    width: 24px;
    height: 24px;
    flex: none;
  }
</style>
</head>
<body>
<div class="canvas">
  <div class="business-card">
    <div class="portrait" role="img" aria-label="Portrait photo of the screenwriter in a red shirt against a warm brown studio backdrop"></div>
    <div class="details">
      <div class="brand">
        <div class="brand-name">Marcus Pell</div>
        <div class="brand-title">Screenwriter</div>
      </div>
      <p class="logline">A brilliant, shrewd Hollywood visionary joins forces with a talented, prolific screen-writer to create wonderful stories and make lots of money together. Make this your story at <span class="site">www.marcuspellwrites.com</span>.</p>
      <ul class="contact-list">
        <li class="contact-item">
          <svg class="contact-icon" viewBox="0 0 24 24" aria-hidden="true">
            <rect width="24" height="24" rx="2" fill="var(--mauve-deep)"/>
            <path d="M8 5.5l2 3-1.3 1.3c.8 1.8 2.2 3.2 4 4L14 12.5l3 2-.9 2.6c-5.2-.4-9-4.3-9.4-9.4z" fill="var(--card-dark)"/>
          </svg>
          <span>555 - 214 - 7386</span>
        </li>
        <li class="contact-item">
          <svg class="contact-icon" viewBox="0 0 24 24" aria-hidden="true">
            <rect width="24" height="24" rx="2" fill="var(--mauve-deep)"/>
            <rect x="5" y="7" width="14" height="10" fill="none" stroke="var(--card-dark)" stroke-width="1.8"/>
            <path d="M5 7l7 6 7-6" fill="none" stroke="var(--card-dark)" stroke-width="1.8"/>
          </svg>
          <span>marcuspell@marcuspellwrites.com</span>
        </li>
        <li class="contact-item">
          <svg class="contact-icon" viewBox="0 0 24 24" aria-hidden="true">
            <rect width="24" height="24" rx="2" fill="var(--mauve-deep)"/>
            <circle cx="12" cy="12" r="6.5" fill="none" stroke="var(--card-dark)" stroke-width="1.6"/>
            <ellipse cx="12" cy="12" rx="2.8" ry="6.5" fill="none" stroke="var(--card-dark)" stroke-width="1.4"/>
            <path d="M5.5 12h13" stroke="var(--card-dark)" stroke-width="1.4"/>
          </svg>
          <span>www.marcuspellwrites.com</span>
        </li>
      </ul>
    </div>
  </div>
</div>
</body>
</html>
```